New Consulting Firm Needs Word Template

We are a new consulting firm that specializes in Veltrix Unified Outcome Planning implementations in need of a new Word template. We need our main document to have the following elements:
• Title Page with our logo and a place for a client logo, a title, sub-title, and author information
• Table of Contents
• Numbered Heading 1 through 5
As an example:
1
1.1
1.1.1
1.1.1.1
• Tables are very important as we use them frequently
• Header with our logo and the client logo
• Footer with page numbers and something about confidential document
• The fonts in the document need to just work, regardless of the computer and in office 365
This template will be used to put together any of the following documents:
• Statement of Work
• Admin Guide
• Design Document
• User Guide
• Requirements Document
• Offer Letter
• Internal Documentation
• Profile/Bio/Resource Resume
Our logo has been uploaded and you can find our website here:
https://brantwellconsulting.example
We would like the main theme colors to blend with our logo, but also have a variety of colors in the theme that complement the main theme colors. I have also uploaded a PDF version of our PowerPoint template.

```html
<!DOCTYPE html>
<html lang="en">
<head>
<meta charset="utf-8">
<title>Brantwell Consulting – Document Template</title>
<link rel="stylesheet" href="https://fonts.googleapis.com/css2?family=Montserrat:wght@700;800&family=Ubuntu:wght@400;500;700&family=Lato:ital,wght@0,400;1,300&display=swap">
<style>
  :root {
    --stage: #000000;
    --brand-blue: #0d4f98;
    --brand-blue-deep: #0a4286;
    --accent-blue: #1f6fba;
    --title-blue: #1a5aa6;
    --paper: #ffffff;
    --paper-soft: #f3f3f4;
    --slate: #5f5f61;
    --rule-gray: #6b6b6d;
    --body-text: #6e6e70;
    --hero-text: #8a8a8c;
    --box-line: #c9c9cb;
  }
  * { margin: 0; padding: 0; box-sizing: border-box; }
  html, body { width: 1200px; height: 779px; overflow: hidden; background: var(--stage); }
  .canvas { position: relative; width: 1200px; height: 779px; }

  .page { position: absolute; top: 8px; width: 585px; height: 755px; background: var(--paper); overflow: hidden; }
  .page--cover { left: 8px; background: var(--paper-soft); }
  .page--content { left: 604px; }

  /* Cover */
  .cover-field {
    position: absolute; left: 0; top: 0; width: 585px; height: 504px;
    background: linear-gradient(135deg, #1460b0 0%, var(--brand-blue) 45%, var(--brand-blue-deep) 100%);
  }
  .cover-title {
    position: absolute; left: 0; width: 100%; top: 283px; text-align: center;
    font-family: "Montserrat", sans-serif; font-weight: 800; font-size: 29px;
    letter-spacing: 0.5px; color: var(--paper);
  }
  .cover-subtitle {
    position: absolute; left: 0; width: 100%; top: 326px; text-align: center;
    font-family: "Ubuntu", sans-serif; font-size: 15.5px; color: var(--paper);
  }
  .firm-mark {
    position: absolute; left: 140px; top: 578px; width: 130px; text-align: center;
    font-family: "Ubuntu", sans-serif; font-weight: 500; color: var(--accent-blue);
  }
  .firm-mark__square { display: block; width: 44px; height: 44px; margin: 0 auto 12px; background: var(--accent-blue); }
  .firm-mark__name { font-size: 15px; letter-spacing: 1.5px; line-height: 1.15; }
  .client-logo-box {
    position: absolute; left: 328px; top: 577px; width: 127px; height: 80px;
    border: 1px solid var(--box-line); background: var(--paper-soft);
    display: flex; align-items: center; justify-content: center; text-align: center;
    font-family: "Ubuntu", sans-serif; font-weight: 700; font-size: 17px; line-height: 21px;
    color: var(--brand-blue);
  }
  .cover-base { position: absolute; left: 0; bottom: 0; width: 100%; height: 24px; background: var(--slate); }

  /* Content page */
  .section-marker { position: absolute; left: 0; top: 14px; width: 5px; height: 19px; background: var(--rule-gray); }
  .section-title {
    position: absolute; left: 12px; top: 13px;
    font-family: "Ubuntu", sans-serif; font-weight: 700; font-size: 19.5px; color: var(--title-blue);
  }
  .header-mark {
    position: absolute; right: 12px; top: 18px; display: flex; align-items: center; gap: 6px;
    font-family: "Ubuntu", sans-serif; font-weight: 500; font-size: 13px; letter-spacing: 1px; color: var(--accent-blue);
  }
  .header-mark__square { width: 16px; height: 16px; background: var(--accent-blue); }
  .hero {
    position: absolute; left: 0; top: 60px; width: 585px; height: 156px;
    background: linear-gradient(90deg, #f1f1f2 0%, #e4e4e6 45%, #ededee 70%, #f4f4f5 100%);
  }
  .hero__quote {
    position: absolute; left: 37px; top: 42px; width: 478px;
    font-family: "Lato", sans-serif; font-style: italic; font-weight: 300;
    font-size: 14.2px; line-height: 22px; color: var(--hero-text);
  }
  .point { position: absolute; left: 37px; width: 510px; }
  .point__title {
    display: flex; align-items: center; gap: 5px;
    font-family: "Ubuntu", sans-serif; font-weight: 700; font-size: 11.3px; color: var(--title-blue);
  }
  .point__icon { width: 14px; height: 14px; background: var(--accent-blue); flex: none; }
  .point__body {
    margin: 3px 0 0 20px; width: 482px;
    font-family: "Lato", sans-serif; font-size: 7.6px; line-height: 11.9px; color: var(--body-text);
  }
  .page-footer { position: absolute; left: 0; bottom: 0; width: 585px; height: 16px; }
  .page-footer svg { position: absolute; left: 0; top: 0; }
  .page-footer__copy {
    position: absolute; left: 6px; top: 2px;
    font-family: "Ubuntu", sans-serif; font-size: 8.5px; color: var(--paper);
  }
  .page-footer__num {
    position: absolute; right: 10px; top: 2px;
    font-family: "Ubuntu", sans-serif; font-size: 8.5px; color: var(--paper);
  }
</style>
</head>
<body>
<main class="canvas">
  <section class="page page--cover">
    <div class="cover-field" role="img" aria-label="Blue background with a faint connected-network pattern"></div>
    <h1 class="cover-title">TEMPLATE TITLE HERE</h1>
    <p class="cover-subtitle">Subtext here Subtext here Subtext here</p>
    <div class="firm-mark">
      <span class="firm-mark__square"></span>
      <span class="firm-mark__name">BRANTWELL<br>CONSULTING</span>
    </div>
    <div class="client-logo-box">CLIENT<br>LOGO HERE</div>
    <div class="cover-base"></div>
  </section>

  <section class="page page--content">
    <span class="section-marker"></span>
    <h2 class="section-title">SECTION TITLE HERE</h2>
    <div class="header-mark"><span class="header-mark__square"></span>BRANTWELL</div>

    <div class="hero" role="img" aria-label="Soft grey photograph of an office tower">
      <p class="hero__quote">Liquorice jelly beans applicake apple pie cupcake brownie bear claw&nbsp; cake gin-gerbread cotton candy. Bear claw croissant apple pie. Croissant cake sweet puff tart . Liquorice jelly beans applicake apple pie cupcake brownie bear claw .</p>
    </div>

    <div class="point" style="top:261px">
      <h3 class="point__title"><span class="point__icon"></span>BULLET TITLE TEXT HERE</h3>
      <p class="point__body">Liquorice jelly beans applicake apple pie cupcake brownie bear claw&nbsp; cake gingerbread cotton candy. Bear claw croissant apple pie. Croissant cake sweet puff tart . Liquorice jelly beans applicake apple pie cupcake brownie bear claw . Liquorice jelly beans applicake apple pie cupcake brownie bear claw&nbsp; cake gingerbread cotton candy. Bear claw croissant apple pie. Croissant cake sweet puff tart . Liquorice jelly beans applicake apple pie cupcake brownie bear claw .</p>
    </div>
    <div class="point" style="top:347px">
      <h3 class="point__title"><span class="point__icon"></span>BULLET TITLE TEXT HERE</h3>
      <p class="point__body">Liquorice jelly beans applicake apple pie cupcake brownie bear claw&nbsp; cake gingerbread cotton candy. Bear claw croissant apple pie. Croissant cake sweet puff tart . Liquorice jelly beans applicake apple pie cupcake brownie bear claw . Liquorice jelly beans applicake apple pie cupcake brownie bear claw&nbsp; cake gingerbread cotton candy. Bear claw croissant apple pie. Croissant cake sweet puff tart . Liquorice jelly beans applicake apple pie cupcake brownie bear claw .</p>
    </div>
    <div class="point" style="top:433px">
      <h3 class="point__title"><span class="point__icon"></span>BULLET TITLE TEXT HERE</h3>
      <p class="point__body">Liquorice jelly beans applicake apple pie cupcake brownie bear claw&nbsp; cake gingerbread cotton candy. Bear claw croissant apple pie. Croissant cake sweet puff tart . Liquorice jelly beans applicake apple pie cupcake brownie bear claw . Liquorice jelly beans applicake apple pie cupcake brownie bear claw&nbsp; cake gingerbread cotton candy. Bear claw croissant apple pie. Croissant cake sweet puff tart . Liquorice jelly beans applicake apple pie cupcake brownie bear claw .</p>
    </div>
    <div class="point" style="top:528px">
      <h3 class="point__title"><span class="point__icon"></span>BULLET TITLE TEXT HERE</h3>
      <p class="point__body">Liquorice jelly beans applicake apple pie cupcake brownie bear claw&nbsp; cake gingerbread cotton candy. Bear claw croissant apple pie. Croissant cake sweet puff tart . Liquorice jelly beans applicake apple pie cupcake brownie bear claw . Liquorice jelly beans applicake apple pie cupcake brownie bear claw&nbsp; cake gingerbread cotton candy. Bear claw croissant apple pie. Croissant cake sweet puff tart . Liquorice jelly beans applicake apple pie cupcake brownie bear claw .</p>
    </div>
    <div class="point" style="top:630px">
      <h3 class="point__title"><span class="point__icon"></span>BULLET TITLE TEXT HERE</h3>
      <p class="point__body">Liquorice jelly beans applicake apple pie cupcake brownie bear claw&nbsp; cake gingerbread cotton candy. Bear claw croissant apple pie. Croissant cake sweet puff tart . Liquorice jelly beans applicake apple pie cupcake brownie bear claw . Liquorice jelly beans applicake apple pie cupcake brownie bear claw&nbsp; cake gingerbread cotton candy. Bear claw croissant apple pie. Croissant cake sweet puff tart . Liquorice jelly beans applicake apple pie cupcake brownie bear claw .</p>
    </div>

    <footer class="page-footer">
      <svg width="585" height="16" viewBox="0 0 585 16" aria-hidden="true">
        <polygon points="0,0 508,0 516,16 0,16" fill="var(--accent-blue)"/>
        <polygon points="525,0 585,0 585,16 533,16" fill="var(--slate)"/>
      </svg>
      <span class="page-footer__copy">Copyright text here</span>
      <span class="page-footer__num">Page: 01</span>
    </footer>
  </section>
</main>
</body>
</html>
```